Wordpress Website for electrician

I'm looking for an easy to maintain website for my electrical contracting business. Need a professional and appealing site.
Im wanting a website where clients can come on and look at services we offer, case studies and advertise our services.
Colours I'm wanting to incorporate are green, white, black and grey
I'm wanting a big slide show on main page where I can place advertising etc.
Menu is to include home, services, our work, specials, energy efficiency and contact
My existing site is www.trelwirefix.com.au
Updates
looking for something with a similar layout to this website
Target Market(s)
Businesses
Industry/Entity Type
Electrician
Look and feel

```html
<!DOCTYPE html>
<html lang="en">
<head>
<meta charset="utf-8">
<title>Trelwire Fix – Electrical Contractor</title>
<link href="https://fonts.googleapis.com/css2?family=Oswald:wght@400;500&family=Cabin:wght@400;600;700&family=Ubuntu:wght@500&family=Open+Sans:wght@800&display=swap" rel="stylesheet">
<style>
:root{
  --green:#3cb54a;
  --green-dark:#2e9a3b;
  --grey-bg:#ececec;
  --grey-nav:#6d6d6d;
  --grey-text:#6b6b6b;
  --grey-footer:#dcdcdc;
  --grey-bar:#a8a8a8;
  --ink:#1d1d1d;
  --white:#ffffff;
  --navy:#0d2b5c;
  --navy-deep:#061a3c;
}
*{margin:0;padding:0;box-sizing:border-box}
html,body{width:1067px;height:1200px;overflow:hidden}
body{background:var(--grey-bg);font-family:'Cabin',sans-serif;color:var(--grey-text);position:relative}
.abs{position:absolute}
.head{font-family:'Oswald',sans-serif;text-transform:uppercase;letter-spacing:-.2px}

/* header */
.brand{left:89px;top:16px;display:flex;align-items:center;gap:10px}
.brand-dot{width:42px;height:42px;border-radius:50%;background:var(--green)}
.brand-name{font-family:'Cabin',sans-serif;font-weight:700;font-size:34px;color:var(--green);line-height:1}
.brand-sub{left:142px;top:58px;font-size:10px;color:#888}
.contact-list{left:769px;top:10px;list-style:none}
.contact-list li{display:flex;align-items:center;gap:10px;height:21.5px;font-family:'Oswald',sans-serif;font-size:14px;color:var(--grey-nav);text-transform:uppercase}
.contact-list svg{width:16px;height:14px}

/* nav */
.nav{left:89px;top:83px;width:889px;height:29px;background:var(--green);display:flex;list-style:none}
.nav li{font-size:10px;color:var(--white);text-transform:uppercase;height:29px;line-height:29px;letter-spacing:.3px}
.nav li.active{background:var(--grey-nav)}

/* slider */
.slider{left:89px;top:112px;width:889px;height:282px;background:linear-gradient(180deg,#1a4ea8,#0a2c6a 55%,#1656b0)}
.slider-band{left:0;top:51px;width:889px;height:174px;background:linear-gradient(90deg,var(--navy-deep),#0e2f66 50%,var(--navy-deep))}
.slider-caption{left:0;top:91px;width:889px;text-align:center;font-family:'Ubuntu',sans-serif;font-weight:500;font-size:26.5px;line-height:32px;color:var(--white);text-shadow:0 2px 4px rgba(0,0,0,.6)}
.slider-arrow{top:115px;width:42px;height:42px;border-radius:50%;background:linear-gradient(#fff,#d6d6d6);box-shadow:0 1px 4px rgba(0,0,0,.5)}
.slider-dots{left:0;top:252px;width:889px;display:flex;justify-content:center;gap:4.5px}
.slider-dots span{width:14px;height:14px;border-radius:50%;background:linear-gradient(#fff,#c9c9c9);box-shadow:0 0 2px rgba(0,0,0,.5)}

/* services */
.service{top:405px;width:263px}
.service-photo{height:126px;box-shadow:0 6px 8px -4px rgba(0,0,0,.45)}
.service h3{margin-top:13px;text-align:center;font-weight:500;font-size:18px;line-height:26px;color:var(--ink)}
.service p{margin-top:2px;padding-left:6px;width:275px;font-size:9.4px;line-height:12.5px;color:#333}

/* content panel */
.panel{left:89px;top:616px;width:889px;height:355px;background:var(--white);box-shadow:0 0 4px rgba(0,0,0,.2)}
.feature h2{font-size:21px;font-weight:500;color:var(--green);line-height:1}
.feature p{font-size:10px;line-height:16px;text-align:justify;margin-top:14px}
.btn{height:22px;line-height:20px;border-radius:2px;font-family:'Oswald',sans-serif;font-size:11.5px;color:var(--white);text-align:center;text-transform:uppercase;letter-spacing:.3px;border:1px solid #222}
.btn-green{background:linear-gradient(#7fe06c,#3cab2c);border-color:#2f7d22}
.btn-dark{background:linear-gradient(#6a6a6a,#262626)}
.rule{width:1px;background:#cfcfcf}
.side-title{font-family:'Oswald',sans-serif;font-size:13.5px;color:var(--ink);text-transform:uppercase}
.side-title em{font-style:normal;color:var(--green)}
.news-item{width:161px;border-bottom:1px dashed #ccc;padding-bottom:5px}
.news-item h4{font-size:10px;font-weight:400;color:var(--green)}
.news-item p{font-size:8.5px;line-height:11.5px;margin-top:3px;text-align:justify}
.more{font-size:9px;color:var(--green)}
.quote{font-size:8.5px;line-height:11.5px;width:160px}
.quote-by{font-size:9.5px;color:var(--green);text-align:right;width:160px}
.quote-by i{color:var(--ink)}
.promo-title{font-family:'Open Sans',sans-serif;font-weight:800;text-align:center;line-height:1}
.ad-text{font-family:'Cabin',sans-serif;font-weight:700}

/* footer */
.footer{left:0;top:985px;width:1067px;height:177px;background:var(--grey-footer);border-top:1px solid #cfcfcf}
.footer-col h5{font-family:'Oswald',sans-serif;font-weight:400;font-size:14px;color:#555;text-transform:uppercase}
.footer-col ul{list-style:none;margin-top:8px}
.footer-col li{font-size:9.5px;height:21.3px;color:#777}
.social{display:flex;gap:8px;margin-top:10px}
.social span{width:27px;height:27px;border-radius:4px;background:#9a9a9a}
.accredit h5{font-family:'Oswald',sans-serif;font-weight:400;font-size:17px;line-height:20px;color:#555;text-align:center;text-transform:uppercase}
.accredit h5 em{font-style:normal;color:var(--green)}
.legal{left:0;top:1162px;width:1067px;height:38px;background:var(--grey-bar);border-top:2px solid #8f8f8f;text-align:center;line-height:34px;font-size:9px;color:var(--white)}
</style>
</head>
<body>

<header>
  <div class="abs brand"><span class="brand-dot"></span><span class="brand-name">trelwirefix</span></div>
  <div class="abs brand-sub">electrical contractor</div>
  <ul class="abs contact-list">
    <li><svg viewBox="0 0 16 12"><rect x="0.5" y="0.5" width="15" height="11" fill="#444"/><path d="M1 1l7 6 7-6" stroke="#fff" fill="none"/></svg>info@trelwirefix.com.au</li>
    <li><svg viewBox="0 0 16 12"><rect x="0.5" y="0.5" width="15" height="11" fill="#444"/><path d="M1 1l7 6 7-6" stroke="#fff" fill="none"/></svg>sales@trelwirefix.com.au</li>
    <li><svg viewBox="0 0 16 14"><rect x="4" y="0" width="8" height="14" rx="1" fill="#444"/><rect x="5.5" y="2" width="5" height="8" fill="#fff"/></svg>Mobile: 0400555018</li>
  </ul>
</header>

<ul class="abs nav">
  <li style="width:71px;padding-left:25px">Home</li>
  <li class="active" style="width:85px;padding-left:22px">Services</li>
  <li style="width:90px;padding-left:21px">Our Work</li>
  <li style="width:85px;padding-left:20px">Specials</li>
  <li style="width:129px;padding-left:14px">Energy Efficiency</li>
  <li style="width:80px;padding-left:18px">Contact</li>
</ul>

<section class="abs slider" role="img" aria-label="Slide: two sparking electrical cables with blue lightning">
  <div class="abs slider-band"></div>
  <p class="abs slider-caption">Every job we do, we take the same approach.<br>To be professional, tidy, deliver a great workmanship<br>and most importantly make the customer happy.</p>
  <div class="abs slider-arrow" style="left:6px"><svg viewBox="0 0 42 42" width="42" height="42"><path d="M24 13l-8 8 8 8" stroke="#333" stroke-width="4" fill="none"/></svg></div>
  <div class="abs slider-arrow" style="left:841px"><svg viewBox="0 0 42 42" width="42" height="42"><path d="M18 13l8 8-8 8" stroke="#333" stroke-width="4" fill="none"/></svg></div>
  <div class="abs slider-dots"><span></span><span></span><span></span><span></span><span></span><span></span><span></span><span></span><span></span><span></span></div>
</section>

<article class="abs service" style="left:89px">
  <div class="service-photo" role="img" aria-label="Cable tray with bundled electrical wiring" style="background:linear-gradient(160deg,#8a6a46,#c7955a 45%,#5a4a3c)"></div>
  <h3 class="head">Electrical Contracting</h3>
  <p>We offer all types of electrical work from Installation to<br>maintenance</p>
</article>
<article class="abs service" style="left:402px">
  <div class="service-photo" role="img" aria-label="Aerial view of solar panels on a warehouse roof" style="background:linear-gradient(160deg,#6f7378,#b9bcc0 50%,#5c5a58)"></div>
  <h3 class="head">Energy Efficiency</h3>
  <p>With one of our audits to your business or home we can<br>lower your energy bills and minimise your carbon footprint</p>
</article>
<article class="abs service" style="left:714px">
  <div class="service-photo" role="img" aria-label="Office meeting room with long table" style="background:linear-gradient(160deg,#1f3555,#35507a 55%,#c9b486)"></div>
  <h3 class="head">Underground Locating</h3>
  <p>We have the tools and knowledge in locating underground<br>utilities.</p>
</article>

<section class="abs panel">
  <div class="abs feature" style="left:13px;top:12px;width:394px">
    <h2 class="head">LED is the future</h2>
    <p>LED lighting has involved rapidly in the last 5 years. In the coming years we will see all lighting being substitued with LED lights. It is by far the most efficient form of lighting on todays market. Let us retrofit your business or home with LED and the savings will literally pay the lights off.</p>
  </div>
  <div class="abs btn btn-green" style="left:182px;top:124px;width:109px">Why LED</div>
  <div class="abs btn btn-dark" style="left:297px;top:124px;width:107px">Request Qoute</div>

  <div class="abs feature" style="left:13px;top:178px;width:394px">
    <h2 class="head">Reduce your business energy consumption</h2>
    <p>By letting us analyse your energy consumption, we can identify where you are simply burning your money. We can suggest and implement easy solutions to save you money and minimise your carbon emmissions.</p>
  </div>
  <div class="abs btn btn-green" style="left:144px;top:276px;width:150px">Energy Efficiency Audit?</div>
  <div class="abs btn btn-dark" style="left:300px;top:276px;width:109px">Book Audit Now</div>

  <div class="abs rule" style="left:429px;top:12px;height:330px"></div>

  <div class="abs side-title" style="left:440px;top:10px">Latest <em>News</em></div>
  <div class="abs news-item" style="left:439px;top:36px"><h4>Electricity Prices Soar</h4><p>The Australian government's carbon tax will see electricity prices soar</p></div>
  <div class="abs news-item" style="left:439px;top:85px"><h4>Electricity Prices Soar</h4><p>The Australian government's carbon tax will see electricity prices soar</p></div>
  <div class="abs news-item" style="left:439px;top:134px"><h4>Electricity Prices Soar</h4><p>The Australian government's carbon tax will see electricity prices soar</p></div>
  <div class="abs more" style="left:555px;top:182px">view more</div>

  <div class="abs side-title" style="left:439px;top:203px">Client <em>Testimonies</em></div>
  <div class="abs" role="img" aria-label="Client portrait" style="left:481px;top:229px;width:65px;height:47px;background:linear-gradient(135deg,#9fb4c8,#d8dde2)"></div>
  <p class="abs quote" style="left:441px;top:282px">Trelwire Fix considerd all our needs and incorparated energy saving</p>
  <p class="abs quote-by" style="left:441px;top:306px">Dan Marsh <i>- Kestrel Group</i></p>
  <div class="abs" style="left:436px;top:322px;width:165px;border-top:1px dashed #ccc"></div>
  <div class="abs more" style="left:557px;top:327px">view more</div>

  <div class="abs rule" style="left:611px;top:12px;height:330px"></div>

  <div class="abs" style="left:619px;top:6px;width:259px;height:200px">
    <div class="abs" role="img" aria-label="Light bulb with a small tree inside" style="left:113px;top:2px;width:34px;height:62px;border-radius:17px 17px 6px 6px;background:linear-gradient(#7cc36b,#d9e8d4 60%,#555)"></div>
    <div class="abs promo-title" style="left:0;top:76px;width:259px;font-size:40px;color:var(--green)">BE GREEN</div>
    <div class="abs promo-title" style="left:0;top:115px;width:259px;font-size:29px;color:var(--ink)">SAVE MONEY</div>
    <div class="abs" role="img" aria-label="Strip of green grass" style="left:0;top:174px;width:259px;height:26px;background:linear-gradient(#9ed37a,#3f8f2c)"></div>
  </div>

  <div class="abs" style="left:619px;top:217px;width:259px;height:120px;background:linear-gradient(#fff,#f1f1f1)">
    <svg class="abs" style="left:0;top:0" width="70" height="90" viewBox="0 0 70 90"><polygon points="40,0 70,0 0,80 0,50" fill="#d91f26"/><text x="18" y="50" transform="rotate(-50 30 40)" font-family="Oswald,sans-serif" font-size="11" fill="#fff">SPECIALS</text></svg>
    <div class="abs" role="img" aria-label="LED downlight products and box" style="left:20px;top:22px;width:72px;height:80px;background:linear-gradient(135deg,#c9c4d6,#8a7aa8 50%,#dcdcdc)"></div>
    <div class="abs ad-text" style="left:85px;top:3px;font-size:19px;color:var(--green)">LED DOWNLIGHTS</div>
    <div class="abs ad-text" style="left:117px;top:25px;font-size:10.5px;color:var(--ink)">Supplied &amp; Installed</div>
    <div class="abs promo-title" style="left:118px;top:50px;font-size:42px;color:var(--green)">$33</div>
    <div class="abs ad-text" style="left:210px;top:54px;font-size:9px;color:var(--green);font-weight:400">EACH</div>
    <div class="abs ad-text" style="left:17px;top:104px;font-size:7px;color:var(--ink)">CONDITIONS APPLY</div>
    <div class="abs ad-text" style="left:107px;top:103px;font-size:9.5px;color:#f0a032;font-weight:600">Click here for more details</div>
  </div>
</section>

<footer class="abs footer">
  <div class="abs footer-col" style="left:91px;top:18px"><h5>About</h5><ul><li>About Trelwire</li><li>What We Do</li><li>Our Philosphy</li><li>Testimonials</li></ul></div>
  <div class="abs footer-col" style="left:203px;top:18px"><h5>Services</h5><ul><li>Electrical Contracting</li><li>Energy Efficiency</li><li>Underground Locating</li></ul></div>
  <div class="abs footer-col" style="left:330px;top:18px"><h5>Our Work</h5><ul><li>Clients</li><li>Photos</li><li>Energy Efficiency Audits</li></ul></div>
  <div class="abs footer-col" style="left:453px;top:18px"><h5>Contact Us</h5><ul><li>info@trelwirefix.com.au</li><li>sales@trelwirefix.com.au</li><li>Mobile: 0400 555 018</li></ul></div>
  <div class="abs footer-col" style="left:608px;top:18px"><h5>Follow us on:</h5><div class="social"><span></span><span></span><span></span><span></span></div></div>
  <div class="abs accredit" style="left:767px;top:14px;width:200px">
    <h5>Proudly accredited<br><em>GreenTrade Electricians</em></h5>
    <div style="width:70px;height:70px;margin:12px auto 0;border-radius:50%;background:#b5b5b5"></div>
    <p style="text-align:center;margin-top:8px;font-size:15px;font-weight:600;color:var(--green)">GreenTrade Electricians</p>
  </div>
</footer>

<div class="abs legal">Trelwire Fix is a Registered Eleectrical Contractor - REC. 48120</div>

</body>
</html>
```